beauty salon application for consumer

- Find your favorite beauty salons and spas or discover new places next to you with geolocation;
- Filter your search by price, distance, category and type of service;
- Never worry again about having to schedule during your work hours or about not having your calls answered when you want to book an appointment;
- Mark salons as favorites and be the first to be informed of exclusive discounts;
- Don’t ever forget your appointments with Glow Slot’s notifications;
- Compare prices, places and services freely, in a quick and practical way;
- Share reviews about services and places you go with other users and read their opinions;
- USER-FRIENDLY INTERFACE
- GALLERY
- OFFERS

similar interface with application name "pamperlane"

Industry/Entity Type

Beauty Salon

Font styles to use
Decorative
Script

Colors

Designer to choose colors to be used in the design.

Requirements
Must have
• Please have a look into these applications:
• 1- https://apps.example-store.test/gb/app/pamperlane/id572913804/?pid=korvasa&c=footer-link
• 2- https://apps.example-store.test/us/app/curlo-ltd-book-curl-style-glam-polish-services/id3948172065
• 3- https://market.sample-apps.test/store/apps/details?id=com.parlorvix.user&hl=en
• 4- https://apps.example-store.test/app/id463187209?mt=8
Nice to have
• Nice to give me a clear screenshots for main function of the application ,please see the above applications before giving me a design .

```html
<!DOCTYPE html>
<html lang="en">
<head>
<meta charset="utf-8">
<title>pamperlane – Search List View</title>
<link href="https://fonts.googleapis.com/css2?family=Montserrat:wght@600;700&family=Rubik:wght@400;500&display=swap" rel="stylesheet">
<style>
  :root {
    --bg-deep: #117a9b;
    --bg-light: #16a497;
    --screen-bg: #ffffff;
    --ink: #1c1c1c;
    --ink-soft: #3a3a3a;
    --muted: #8a8a8a;
    --field: #ececec;
    --link-blue: #1f6f95;
    --price-ink: #1a6e8e;
    --star-on: #f39200;
    --star-off: #c9c9c9;
    --fab: #0f8f9e;
    --label-line: #ffffff;
  }
  * { box-sizing: border-box; margin: 0; padding: 0; }
  html, body { width: 1200px; height: 1200px; overflow: hidden; }
  body {
    font-family: "Rubik", "Helvetica Neue", Arial, sans-serif;
    background: linear-gradient(160deg, var(--bg-deep) 0%, #128ea0 50%, var(--bg-light) 100%);
    position: relative;
  }

  .app-screen {
    position: absolute;
    left: 130px; top: 200px;
    width: 450px; height: 800px;
    background: var(--screen-bg);
    overflow: hidden;
    box-shadow: 0 20px 50px rgba(0,0,0,.25);
  }

  .status-bar {
    height: 27px;
    display: flex; align-items: center; justify-content: space-between;
    padding: 0 8px;
    font-size: 13px; color: var(--ink-soft);
  }
  .status-bar .left, .status-bar .right { display: flex; align-items: center; gap: 4px; width: 120px; }
  .status-bar .right { justify-content: flex-end; }

  .search-row {
    height: 46px;
    display: flex; align-items: center;
    padding: 0 14px 0 16px;
    gap: 18px;
  }
  .search-field {
    flex: 1;
    height: 42px;
    background: var(--field);
    border-radius: 21px;
    display: flex; align-items: center; gap: 14px;
    padding: 0 16px;
    font-size: 19px; color: var(--ink);
  }

  .location-row {
    height: 50px;
    display: flex; align-items: center; justify-content: space-between;
    padding: 0 18px;
    font-size: 19px; color: var(--muted);
  }
  .location-row .city { color: var(--link-blue); font-weight: 500; }

  .salon-photo { height: 240px; }
  .salon-photo.reception { background: linear-gradient(120deg, #5a3a22 0%, #b07a3a 45%, #3d5f7a 75%, #1c2b3a 100%); }
  .salon-photo.stations { background: linear-gradient(180deg, #7a4a3a 0%, #b98a68 45%, #d9c3ad 100%); }

  .salon-info {
    position: relative;
    padding: 16px 18px 0;
    height: 102px;
  }
  .salon-info.last { height: 94px; }
  .salon-name { font-size: 20px; font-weight: 500; color: var(--ink); }
  .salon-address { font-size: 17px; color: var(--ink-soft); margin-top: 4px; }
  .stars { display: flex; gap: 8px; margin-top: 8px; }
  .price-pill {
    position: absolute; right: 18px; top: 30px;
    width: 108px; height: 40px;
    border-radius: 20px;
    background: var(--field);
    display: flex; align-items: center; justify-content: center;
    font-size: 19px; font-weight: 500; color: var(--price-ink);
  }

  .filter-fab {
    position: absolute; left: 360px; top: 710px;
    width: 72px; height: 72px; border-radius: 50%;
    background: var(--fab);
    display: flex; align-items: center; justify-content: center;
    box-shadow: 0 4px 10px rgba(0,0,0,.3);
  }

  .view-label {
    position: absolute;
    left: 684px; top: 249px;
    width: 452px; height: 86px;
    border: 2px solid var(--label-line);
    border-radius: 43px;
    display: flex; align-items: center; justify-content: center;
    font-family: "Montserrat", Arial, sans-serif;
    font-weight: 700; font-size: 34px;
    letter-spacing: 2.5px;
    color: var(--label-line);
  }
</style>
</head>
<body>

<section class="app-screen" aria-label="pamperlane search results list">
  <div class="status-bar">
    <div class="left">
      <svg width="20" height="11" viewBox="0 0 20 11"><rect x="0" y="7" width="3" height="4" fill="#333"/><rect x="5" y="5" width="3" height="6" fill="#333"/><rect x="10" y="2" width="3" height="9" fill="#333"/><rect x="15" y="0" width="3" height="11" fill="#333"/></svg>
      <span>Nexa</span>
      <svg width="14" height="11" viewBox="0 0 14 11"><path d="M1 4a9 9 0 0 1 12 0M3 6.5a6 6 0 0 1 8 0M5 9a3 3 0 0 1 4 0" stroke="#333" stroke-width="1.6" fill="none"/></svg>
    </div>
    <span>9:41 AM</span>
    <div class="right">
      <span>100%</span>
      <svg width="28" height="12" viewBox="0 0 28 12"><rect x="0.5" y="0.5" width="24" height="11" rx="2" fill="none" stroke="#333"/><rect x="2" y="2" width="21" height="8" fill="#333"/><rect x="25.5" y="4" width="2" height="4" fill="#333"/></svg>
    </div>
  </div>

  <div class="search-row">
    <svg width="20" height="20" viewBox="0 0 20 20"><path d="M2 2l16 16M18 2L2 18" stroke="#333" stroke-width="2.4"/></svg>
    <div class="search-field">
      <svg width="20" height="20" viewBox="0 0 20 20"><circle cx="8" cy="8" r="6.5" stroke="#444" stroke-width="2" fill="none"/><path d="M13 13l6 6" stroke="#444" stroke-width="2.2"/></svg>
      <span>haircut for men</span>
    </div>
    <svg width="28" height="28" viewBox="0 0 28 28"><path d="M14 2a6 6 0 0 1 6 6c0 5-6 11-6 11S8 13 8 8a6 6 0 0 1 6-6z" fill="none" stroke="#333" stroke-width="2"/><circle cx="14" cy="8" r="2" fill="#333"/><path d="M2 26l4-8h4M18 18h4l4 8z M2 26h24" fill="none" stroke="#333" stroke-width="2"/></svg>
  </div>

  <div class="location-row">
    <span>in <span class="city">Vancouver, Canada</span></span>
    <svg width="12" height="18" viewBox="0 0 12 18"><path d="M2 2l7 7-7 7" stroke="#333" stroke-width="2" fill="none"/></svg>
  </div>

  <div class="salon-photo reception" role="img" aria-label="Photo of the salon reception desk with staff and product shelves"></div>
  <div class="salon-info">
    <div class="salon-name">Verano Salon and Spa</div>
    <div class="salon-address">418 W 9th Ave, Vancouver</div>
    <div class="stars">
      <svg width="20" height="20" viewBox="0 0 24 24"><path d="M12 1l3.3 7 7.7.8-5.8 5.2 1.7 7.6L12 17.8 5.1 21.6l1.7-7.6L1 8.8 8.7 8z" fill="var(--star-on)"/></svg>
      <svg width="20" height="20" viewBox="0 0 24 24"><path d="M12 1l3.3 7 7.7.8-5.8 5.2 1.7 7.6L12 17.8 5.1 21.6l1.7-7.6L1 8.8 8.7 8z" fill="var(--star-on)"/></svg>
      <svg width="20" height="20" viewBox="0 0 24 24"><path d="M12 1l3.3 7 7.7.8-5.8 5.2 1.7 7.6L12 17.8 5.1 21.6l1.7-7.6L1 8.8 8.7 8z" fill="var(--star-on)"/></svg>
      <svg width="20" height="20" viewBox="0 0 24 24"><path d="M12 1l3.3 7 7.7.8-5.8 5.2 1.7 7.6L12 17.8 5.1 21.6l1.7-7.6L1 8.8 8.7 8z" fill="var(--star-off)"/></svg>
      <svg width="20" height="20" viewBox="0 0 24 24"><path d="M12 1l3.3 7 7.7.8-5.8 5.2 1.7 7.6L12 17.8 5.1 21.6l1.7-7.6L1 8.8 8.7 8z" fill="var(--star-off)"/></svg>
    </div>
    <div class="price-pill">$15.00</div>
  </div>

  <div class="salon-photo stations" role="img" aria-label="Photo of a row of styling chairs and mirrors in a beauty salon"></div>
  <div class="salon-info last">
    <div class="salon-name">Marisol’s Beauty Care</div>
    <div class="salon-address">3716 Elm St, Vancouver</div>
    <div class="stars">
      <svg width="20" height="20" viewBox="0 0 24 24"><path d="M12 1l3.3 7 7.7.8-5.8 5.2 1.7 7.6L12 17.8 5.1 21.6l1.7-7.6L1 8.8 8.7 8z" fill="var(--star-on)"/></svg>
      <svg width="20" height="20" viewBox="0 0 24 24"><path d="M12 1l3.3 7 7.7.8-5.8 5.2 1.7 7.6L12 17.8 5.1 21.6l1.7-7.6L1 8.8 8.7 8z" fill="var(--star-on)"/></svg>
      <svg width="20" height="20" viewBox="0 0 24 24"><path d="M12 1l3.3 7 7.7.8-5.8 5.2 1.7 7.6L12 17.8 5.1 21.6l1.7-7.6L1 8.8 8.7 8z" fill="var(--star-on)"/></svg>
      <svg width="20" height="20" viewBox="0 0 24 24"><path d="M12 1l3.3 7 7.7.8-5.8 5.2 1.7 7.6L12 17.8 5.1 21.6l1.7-7.6L1 8.8 8.7 8z" fill="var(--star-on)"/></svg>
      <svg width="20" height="20" viewBox="0 0 24 24"><path d="M12 1l3.3 7 7.7.8-5.8 5.2 1.7 7.6L12 17.8 5.1 21.6l1.7-7.6L1 8.8 8.7 8z" fill="var(--star-off)"/></svg>
    </div>
    <div class="price-pill">$18.00</div>
  </div>

  <div class="filter-fab" aria-label="Filter results">
    <svg width="30" height="30" viewBox="0 0 30 30"><path d="M2 4h26L18 15v11l-6-3v-8z" fill="#ffffff"/></svg>
  </div>
</section>

<div class="view-label">SEARCH - LIST VIEW</div>

</body>
</html>
```